Business Card Design Project

New business card design front and back for IT company that does network support and web design.
Calloway IT
Doug Calloway
Managing Director
PO Box 918 Brinsley VIC 3421
doug@callowayit.example
www.callowayit.example

Industry/Entity Type

Business

```html
<!DOCTYPE html>
<html lang="en">
<head>
<meta charset="utf-8">
<title>Calloway IT – Business Card Back</title>
<link rel="stylesheet" href="https://fonts.googleapis.com/css2?family=Bebas+Neue&family=Jost:wght@400&display=swap">
<style>
  :root {
    --card-bg: #ffffff;
    --name-blue: #3fb0d6;
    --text-dark: #1f1f1f;
  }
  * { margin: 0; padding: 0; box-sizing: border-box; }
  html, body {
    width: 1200px;
    height: 694px;
    overflow: hidden;
    background: var(--card-bg);
  }
  .card {
    position: relative;
    width: 1200px;
    height: 694px;
    background: var(--card-bg);
  }
  .contact {
    position: absolute;
    left: 0;
    right: 0;
    top: 212px;
    width: 1184px;
    text-align: center;
  }
  .contact__name {
    font-family: "Bebas Neue", "Oswald", sans-serif;
    font-weight: 400;
    font-size: 70px;
    line-height: 1;
    color: var(--name-blue);
    letter-spacing: 0.5px;
  }
  .contact__details {
    margin-top: 10px;
    font-family: "Jost", "Futura", sans-serif;
    font-weight: 400;
    font-size: 38px;
    line-height: 48px;
    color: var(--text-dark);
    list-style: none;
  }
</style>
</head>
<body>
  <main class="card">
    <section class="contact">
      <h1 class="contact__name">Doug Calloway</h1>
      <ul class="contact__details">
        <li class="contact__role">Managing Director</li>
        <li class="contact__address">PO Box 918 Brinsley</li>
        <li class="contact__address">VIC 3421</li>
        <li class="contact__phone">0400 555 128</li>
      </ul>
    </section>
  </main>
</body>
</html>
```